First North America Product Category Rule

8 x 10 foot booth design for a stretch fabric wrap-around. The booth will be used in a very small exhibit area for 150 attendees. It is for the packaging industry focused on the environment. This booth graphic is NOT about our company, but to promote participation in a project we are sponsoring. The project is to develop the first North American Packaging Category Rule, so the booth is to invite conference attendees to join our effort. Production specifications are attached.

Target Market(s)

Zenith 400, Sustainability Directors, Packaging Engineers

Industry/Entity Type

Packaging; Environment

Font styles to use
Sans Serif

Requirements
Must have
• An Eye-Catching or Intriguing Image/Graphics/Letter Treatment
Should not have
• Nothing too bright or garish. All text should be above waist height (No text below the 36-40" mark)

```html
<!DOCTYPE html>
<html lang="en">
<head>
<meta charset="utf-8">
<title>First North American PCR – Booth Graphic</title>
<link href="https://fonts.googleapis.com/css2?family=Oswald:wght@600;700&family=Montserrat:wght@300;400;600;700;800&display=swap" rel="stylesheet">
<style>
  :root {
    --sky: #0aabd6;
    --slate: #525e6e;
    --leaf: #5db246;
    --tangerine: #f18022;
    --white: #ffffff;
    --page: #ffffff;
    --ink: #3f4754;
  }
  * { margin: 0; padding: 0; box-sizing: border-box; }
  html, body { width: 910px; height: 1200px; overflow: hidden; background: var(--page); }
  .canvas { position: relative; width: 910px; height: 1200px; }
  .booth-graphic {
    position: absolute;
    left: 15px; top: 351px;
    width: 1312px; height: 742px;
    transform: scale(0.6707);
    transform-origin: 0 0;
    overflow: hidden;
    background: var(--sky);
    font-family: "Montserrat", sans-serif;
    color: var(--white);
  }
  .backdrop { position: absolute; inset: 0; }
  .headline {
    position: absolute; left: 110px; width: 500px; top: 58px;
    text-align: center;
    font-family: "Oswald", sans-serif; font-weight: 700; font-style: italic;
    font-size: 50px; line-height: 62px; letter-spacing: 0.5px;
  }
  .tag-pill {
    position: absolute; left: 200px; top: 205px; width: 323px; height: 40px;
    border-radius: 20px; background: var(--tangerine);
    text-align: center; line-height: 40px;
    font-weight: 700; font-size: 21px; letter-spacing: 0.3px;
  }
  .project-title {
    position: absolute; left: 110px; width: 500px; top: 255px; text-align: center;
    font-weight: 800; font-size: 25px; line-height: 34px;
  }
  .project-subtitle {
    position: absolute; left: 110px; width: 500px; top: 290px; text-align: center;
    font-weight: 300; font-size: 25px; line-height: 34px; letter-spacing: 0.5px;
  }
  .signup-button {
    position: absolute; left: 259px; top: 344px; width: 205px; height: 42px;
    border-radius: 21px; background: var(--white); color: var(--ink);
    text-align: center; line-height: 42px;
    font-family: "Oswald", sans-serif; font-weight: 700; font-size: 29px;
  }
  .sponsor-line {
    position: absolute; left: 90px; width: 540px; top: 408px; text-align: center;
    font-size: 15.5px; line-height: 22px; font-weight: 300;
  }
  .sponsor-line strong { font-weight: 700; }
  .pull-quote {
    position: absolute; left: 800px; width: 410px; top: 40px; text-align: center;
    font-weight: 700; font-size: 14.5px; line-height: 20px;
  }
  .quote-mark {
    font-family: "Oswald", sans-serif; font-size: 34px; line-height: 0;
    font-weight: 700; position: relative; top: 10px;
  }
  .step-label {
    position: absolute; width: 130px; text-align: center;
    font-weight: 700; font-size: 12px; line-height: 16px;
  }
  .step-number {
    position: absolute; font-weight: 700; font-size: 20px; line-height: 20px;
  }
</style>
</head>
<body>
<div class="canvas">
  <section class="booth-graphic">
    <svg class="backdrop" viewBox="0 0 1312 742" width="1312" height="742" aria-hidden="false">
      <!-- slate wave -->
      <path d="M0 180 C 120 40, 280 0, 400 12 C 560 30, 700 140, 840 180 C 980 215, 1150 250, 1312 218 L1312 560 C 1180 680, 1060 740, 950 730 C 780 715, 620 480, 400 460 C 250 448, 100 455, 0 470 Z" fill="var(--slate)"/>
      <!-- sky band -->
      <path d="M0 455 C 150 440, 320 440, 460 470 C 650 515, 820 700, 980 712 C 1110 722, 1230 620, 1312 520 L1312 742 L0 742 Z" fill="var(--sky)"/>
      <!-- leaf bottom -->
      <path d="M0 525 C 200 490, 420 500, 560 545 C 720 600, 860 730, 1000 735 C 1140 740, 1240 640, 1312 560 L1312 742 L0 742 Z" fill="var(--leaf)"/>
      <path d="M0 525 C 200 490, 420 500, 560 545 C 720 600, 860 730, 1000 735 C 1140 740, 1240 640, 1312 560" fill="none" stroke="var(--white)" stroke-width="3"/>
      <!-- portrait ring -->
      <circle cx="1008" cy="405" r="278" fill="var(--tangerine)"/>
      <circle cx="1008" cy="405" r="232" fill="var(--white)"/>
      <circle cx="1008" cy="405" r="226" fill="#7b8a99"/>
      <defs>
        <radialGradient id="portraitTone" cx="50%" cy="55%" r="60%">
          <stop offset="0%" stop-color="#d9e25a"/>
          <stop offset="55%" stop-color="#8d97a2"/>
          <stop offset="100%" stop-color="#3d5a86"/>
        </radialGradient>
      </defs>
      <circle cx="1008" cy="405" r="226" fill="url(#portraitTone)" role="img" aria-label="Photo of a smiling warehouse worker in a hi-vis vest holding a hard hat and tablet"/>
      <!-- four-step cluster -->
      <g stroke="var(--white)" stroke-width="6">
        <path d="M720 355 L650 355 A72 72 0 0 1 577 283 A72 72 0 0 1 650 210 A72 72 0 0 1 720 283 Z" fill="var(--leaf)"/>
        <path d="M720 355 L720 283 A72 72 0 0 1 792 210 A72 72 0 0 1 864 283 A72 72 0 0 1 792 355 Z" fill="var(--tangerine)"/>
        <path d="M720 355 L792 355 A72 72 0 0 1 864 428 A72 72 0 0 1 792 500 A72 72 0 0 1 720 428 Z" fill="var(--sky)"/>
        <path d="M720 355 L720 428 A72 72 0 0 1 650 500 A72 72 0 0 1 577 428 A72 72 0 0 1 650 355 Z" fill="var(--slate)"/>
      </g>
    </svg>

    <h1 class="headline">Enlisting Stakeholder<br>Participation</h1>
    <div class="tag-pill">FIRST NORTH AMERICAN</div>
    <p class="project-title">Product Category Rule (PCR)</p>
    <p class="project-subtitle">For Protective Packaging</p>
    <div class="signup-button">SIGN UP NOW!</div>
    <p class="sponsor-line">Sponsored by <strong>Foam Packaging Council Managed</strong><br><strong>by Open Material Ledger</strong></p>

    <p class="pull-quote"><span class="quote-mark">“</span> How EPD Can Move the Dialogue Beyond<br>End-of-Life Disposal to Include<br>Environmental Benchmarks for Product<br>Production &amp; Distribution <span class="quote-mark">”</span></p>

    <p class="step-label" style="left:585px; top:253px;">PCR<br>Product Category<br>Rules</p>
    <p class="step-label" style="left:728px; top:253px;">LCA<br>Life Cycle<br>Assessment</p>
    <p class="step-label" style="left:728px; top:408px;">Third<br>Party<br>Verification</p>
    <p class="step-label" style="left:585px; top:408px;">EPD<br>Registration and<br>Publication</p>
    <span class="step-number" style="left:686px; top:322px;">01</span>
    <span class="step-number" style="left:729px; top:322px;">02</span>
    <span class="step-number" style="left:729px; top:368px;">03</span>
    <span class="step-number" style="left:686px; top:368px;">04</span>
  </section>
</div>
</body>
</html>
```